I want a business card that is going to show a creative spark but without limiting me to an industry. Something edgy but that wont go out of date. I want it state My business name Serafina Loire, profession - Professional Makeup Artist contact number and email

My service is to provide makeup services from bridal, fashion, photography, film, TV and so on. It is creative and different so i want that to be reflected.

I would like the card double sided.
Updates

 I would LOVE a background on my card something like this image... i can supply an image to be formed like this

Please use the image uploaded

Can we try using the image provided on one side of the card and then writing and details on the other side

Target Market(s)

I am targeting a wide range of people from Creative directors to the individual eg. bride

Industry/Entity Type

Business

Requirements
Must have
• Name: Delphine Hartwell
contact numbe 0417853120
email address:info@serafinaloire.com
website: www.serafinaloire.com
One of the images attached

professional makeup artist / hair stylist

I want it to show creativity
Nice to have
• logo, Double-sided card
Should not have
• the design should not use tradional style. Or images that are not my own

```html
<!DOCTYPE html>
<html lang="en">
<head>
<meta charset="utf-8">
<title>Serafina Loire – Business Card</title>
<link href="https://fonts.googleapis.com/css2?family=Comfortaa:wght@300;400&family=Poiret+One&display=swap" rel="stylesheet">
<style>
  :root {
    --stage-light: #6e6e6e;
    --stage-dark: #2e2e2e;
    --teal: #17c3cc;
    --teal-deep: #0d6b72;
    --ink: #000000;
    --purple: #3f3584;
    --purple-soft: #6a5cb0;
    --paper-light: #f2f2f2;
    --paper-mid: #dcdcdc;
    --paper-edge: #9c9c9c;
  }
  * { margin: 0; padding: 0; box-sizing: border-box; }
  html, body { width: 1200px; height: 1128px; overflow: hidden; }
  body {
    background: radial-gradient(ellipse at 50% 0%, var(--stage-light) 0%, #4a4a4a 55%, var(--stage-dark) 100%);
    font-family: "Poiret One", "Comfortaa", sans-serif;
  }
  .stage { position: relative; width: 1200px; height: 1128px; }

  .card {
    position: absolute;
    left: 135px;
    width: 930px;
    height: 484px;
    border-radius: 30px;
    box-shadow: 6px 8px 14px rgba(0,0,0,0.55);
    overflow: hidden;
  }
  .card--front {
    top: 19px;
    background: radial-gradient(ellipse 70% 110% at 18% 25%, #17787e 0%, var(--teal-deep) 30%, #063236 60%, var(--ink) 85%);
  }
  .card--back {
    top: 598px;
    background: radial-gradient(ellipse 65% 80% at 50% 45%, var(--paper-light) 0%, var(--paper-mid) 60%, var(--paper-edge) 100%);
  }

  .brand-dot {
    position: absolute;
    border-radius: 50%;
    background: var(--purple-soft);
  }
  .card--front .brand-dot { left: 60px; top: 183px; width: 150px; height: 150px; }
  .card--back .brand-dot { left: 37px; top: 46px; width: 104px; height: 104px; }

  .brand-name {
    position: absolute;
    font-family: "Poiret One", sans-serif;
    color: var(--teal);
    letter-spacing: 2px;
    white-space: nowrap;
    line-height: 1;
  }
  .brand-role {
    position: absolute;
    font-family: "Comfortaa", sans-serif;
    font-weight: 300;
    color: var(--teal);
    white-space: nowrap;
    line-height: 1;
  }
  .card--front .brand-name { left: 296px; top: 206px; font-size: 70px; }
  .card--front .brand-role { left: 339px; top: 272px; font-size: 35px; }
  .card--back .brand-name { left: 203px; top: 33px; font-size: 66px; }
  .card--back .brand-role { left: 245px; top: 94px; font-size: 34px; }

  .contact {
    position: absolute;
    left: 38px;
    color: var(--purple);
    font-family: "Poiret One", sans-serif;
    font-size: 62px;
    letter-spacing: 3px;
    white-space: nowrap;
    line-height: 1;
  }
  .contact--phone { top: 200px; }
  .contact--email { top: 318px; }
  .contact__cont { display: block; text-align: right; padding-right: 0; margin-top: 16px; width: 850px; }

  .side-label {
    position: absolute;
    font-family: "Comfortaa", sans-serif;
    font-weight: 300;
    color: var(--teal);
    font-size: 118px;
    line-height: 1;
    white-space: nowrap;
  }
  .side-label--front { left: 1072px; top: 72px; transform-origin: 0 0; transform: translate(118px, 0) rotate(90deg); }
  .side-label--back { left: 8px; top: 1035px; transform-origin: 0 0; transform: rotate(-90deg); }
</style>
</head>
<body>
  <main class="stage">
    <section class="card card--front" aria-label="Card front">
      <span class="brand-dot"></span>
      <h1 class="brand-name">Serafina Loire</h1>
      <p class="brand-role">Professional Makeup Artist</p>
    </section>
    <div class="side-label side-label--front">Front</div>

    <section class="card card--back" aria-label="Card back">
      <span class="brand-dot"></span>
      <h2 class="brand-name">Serafina Loire</h2>
      <p class="brand-role">Professional Makeup Artist</p>
      <p class="contact contact--phone">•Number | 041·785·3120</p>
      <p class="contact contact--email">•Email | SerafinaLoire@<span class="contact__cont">inboxmail.com.au</span></p>
    </section>
    <div class="side-label side-label--back">Back</div>
  </main>
</body>
</html>
```